Home Security Company Business Card

Looking for a eye catching business card that is non traditional and stands out but yet still looks professional. It should include all the pertinent information such as name, title, address, telephone, e-mail, website address should definitely stand out and then finally the logo.

Target Market(s)

Residential and Commercial accounts mostly upscale accounts

Industry/Entity Type

Security

Contact Information for Business Card

Name
Title
Address
Office #
Cell #
E-mail
Website

Font styles to use
Serif
Sans Serif

Requirements
Must have
• Logo, two sided color configuration
Nice to have
• You decide
Should not have
• There really aren't any.

```html
<!DOCTYPE html>
<html lang="en">
<head>
<meta charset="utf-8">
<title>Ironvale Security Systems Inc. — Business Card</title>
<link rel="stylesheet" href="https://fonts.googleapis.com/css2?family=PT+Sans:wght@400;700&family=Tinos:ital,wght@0,400;1,400&display=swap">
<style>
  :root {
    --stage: #3a3a3a;
    --card-red: #7a0f05;
    --card-red-deep: #6a0c03;
    --back-red: #8a1a0c;
    --paper: #ffffff;
    --gold: #e2a63a;
    --ink-light: #ffffff;
    --brand-red: #7a1306;
  }
  * { margin: 0; padding: 0; box-sizing: border-box; }
  html, body {
    width: 1200px; height: 750px; overflow: hidden;
    background: var(--stage);
  }
  .stage { position: relative; width: 1200px; height: 750px; }

  .card {
    position: absolute; top: 228px;
    width: 461px; height: 262px; overflow: hidden;
  }
  .card--front { left: 144px; background: var(--card-red); }
  .card--back  { left: 612px; background: var(--back-red); }

  .card__shapes { position: absolute; inset: 0; width: 461px; height: 262px; }

  .contact {
    position: absolute; left: 36px; top: 48px;
    font-family: "PT Sans", sans-serif; color: var(--ink-light);
  }
  .contact__name { font-size: 17px; font-weight: 700; color: var(--gold); line-height: 1.1; }
  .contact__title { font-size: 13px; line-height: 1.3; }
  .contact__address { margin-top: 24px; font-size: 11.5px; line-height: 1.25; }
  .contact__list { list-style: none; margin-top: 7px; font-size: 11.5px; }
  .contact__list li { display: flex; align-items: center; height: 17.5px; }
  .contact__icon { width: 12px; height: 12px; margin-right: 6px; flex: none; }

  .brand {
    position: absolute; left: 252px; top: 28px;
    display: flex; align-items: center; gap: 8px;
    font-family: "Tinos", serif; font-weight: 400; color: var(--brand-red);
  }
  .brand__dot { width: 64px; height: 64px; border-radius: 50%; background: var(--gold); flex: none; }
  .brand__name { font-size: 22px; line-height: 1; }
  .brand__sub { font-size: 8.6px; line-height: 1.2; }

  .back__pattern { position: absolute; inset: 0; background: radial-gradient(ellipse at center, #941f10 0%, var(--back-red) 70%); }
  .back__brand {
    position: absolute; left: 0; right: 0; top: 106px; text-align: center;
    font-family: "Tinos", serif; font-weight: 400; color: var(--ink-light);
  }
  .back__name { font-size: 36px; line-height: 1; letter-spacing: 1.5px; }
  .back__sub { font-size: 17px; line-height: 1.1; }
  .back__web {
    margin-top: 4px; font-family: "Tinos", serif; font-style: italic;
    font-size: 11.5px; letter-spacing: 8.5px; color: var(--ink-light);
  }
</style>
</head>
<body>
<main class="stage">

  <section class="card card--front" aria-label="Business card front">
    <svg class="card__shapes" viewBox="0 0 461 262" aria-hidden="true">
      <path d="M157 0 H461 V262 H404 C320 190 200 135 157 0 Z" fill="var(--paper)"/>
      <path d="M186 55 C215 150 300 200 395 262 H404 C320 200 220 150 186 55 Z" fill="var(--gold)"/>
      <path d="M190 62 C225 160 310 205 352 262 H360 C310 205 225 160 190 62 Z" fill="var(--card-red-deep)"/>
    </svg>

    <div class="contact">
      <p class="contact__name">Daniel Reyes</p>
      <p class="contact__title">CEO/Founder</p>
      <p class="contact__address">4120 Birchwood Court<br>Fairhaven, Alaska 99508</p>
      <ul class="contact__list">
        <li>
          <svg class="contact__icon" viewBox="0 0 12 12" aria-hidden="true"><path d="M2 1 L4 1 L5 4 L3.6 5 C4.3 6.6 5.4 7.7 7 8.4 L8 7 L11 8 L11 10 C11 10.6 10.6 11 10 11 C5 11 1 7 1 2 C1 1.4 1.4 1 2 1 Z" fill="var(--gold)"/></svg>
          555 214 7830
        </li>
        <li>
          <svg class="contact__icon" viewBox="0 0 12 12" aria-hidden="true"><rect x="3" y="0.5" width="6.5" height="11" rx="1" fill="none" stroke="var(--gold)" stroke-width="1.3"/><rect x="4.3" y="2" width="4" height="6.5" fill="var(--gold)"/></svg>
          555 309 4417
        </li>
        <li>
          <svg class="contact__icon" viewBox="0 0 12 12" aria-hidden="true"><rect x="0.5" y="2.5" width="11" height="7.5" fill="var(--gold)"/><path d="M0.5 2.5 L6 7 L11.5 2.5" fill="none" stroke="var(--card-red)" stroke-width="1"/></svg>
          info@ironvale.com
        </li>
        <li>
          <svg class="contact__icon" viewBox="0 0 12 12" aria-hidden="true"><circle cx="6" cy="6" r="5.5" fill="var(--gold)"/><path d="M1 6 H11 M6 0.5 C3.5 3 3.5 9 6 11.5 M6 0.5 C8.5 3 8.5 9 6 11.5" fill="none" stroke="var(--card-red)" stroke-width="0.8"/></svg>
          www.ironvale.com
        </li>
      </ul>
    </div>

    <div class="brand">
      <span class="brand__dot" aria-hidden="true"></span>
      <div>
        <p class="brand__name">IRONVALE</p>
        <p class="brand__sub">SECURITY SYSTEMS INC.</p>
      </div>
    </div>
  </section>

  <section class="card card--back" aria-label="Business card back">
    <div class="back__pattern" role="img" aria-label="Repeating tonal shield pattern in deep red"></div>
    <div class="back__brand">
      <p class="back__name">IRONVALE</p>
      <p class="back__sub">SECURITY SYSTEMS INC.</p>
      <p class="back__web">www.ironvale.com</p>
    </div>
  </section>

</main>
</body>
</html>
```